Marlow Ridgeway a PlateWork Fabricator! Pressure Vessels, Stainless Vessels, Steel Fabricator!

Update and modernize the www.marlowridgeway.example website. Basically throwing away the old site and coming back with a new feel, new look, but some of the same content. One of our other companies is www.keltonbuilders.example and if you view that site you will get a idea of how we would like the site to feel. Below are the MR logos and the colors are #231F20 and #6D0B17 and the font is Ethnocentric Rg.

Target Market(s)

Steel Fabrication, Platework, Vessel Fabrication,

Industry/Entity Type

Steel

Coding

Coded - Design and coding required

Number of Pages Required

5+ page

Font styles to use
Other font styles liked:
• Ethnocentric Rg

Requirements
Must have
• Industry feel... site must flow and color scheme and font be consistent.

```html
<!DOCTYPE html>
<html lang="en">
<head>
<meta charset="utf-8">
<title>Marlow Ridgeway — Plate Work Fabrication</title>
<link rel="stylesheet" href="https://fonts.googleapis.com/css2?family=Orbitron:wght@700;900&family=Montserrat:wght@400;500;600;700&family=Open+Sans:wght@400;600;700&display=swap">
<style>
  :root {
    --ink: #231F20;
    --brand-red: #6D0B17;
    --button-red: #8E0F1E;
    --white: #FFFFFF;
    --services-bg: #2C2728;
    --footer-bg: #3D3839;
    --rivet-band: #3A3637;
    --muted: #D8D4D5;
    --divider: #4A4546;
  }
  * { box-sizing: border-box; margin: 0; padding: 0; }
  html, body { width: 1200px; height: 2276px; overflow: hidden; }
  body { position: relative; background: var(--ink); font-family: "Montserrat", sans-serif; color: var(--white); }

  /* Header */
  .site-header { position: absolute; left: 0; top: 0; width: 1200px; height: 86px; background: var(--white); }
  .brand { position: absolute; left: 133px; top: 9px; display: flex; align-items: center; gap: 9px; }
  .brand-dot { width: 62px; height: 62px; border-radius: 50%; background: var(--brand-red); flex: none; }
  .brand-name { font-family: "Montserrat", sans-serif; font-weight: 700; font-size: 22px; color: var(--ink); letter-spacing: .5px; line-height: 1; text-transform: uppercase; }
  .brand-name span { display: block; }
  .call-line { position: absolute; right: 310px; top: 12px; display: flex; align-items: center; gap: 8px; font-size: 13.5px; color: var(--ink); }
  .call-line .number { font-size: 18px; color: var(--brand-red); font-weight: 500; }
  .quote-btn { position: absolute; left: 922px; top: 0; width: 146px; height: 36px; background: var(--brand-red); color: var(--white); font-size: 11px; font-weight: 700; display: flex; align-items: center; justify-content: center; letter-spacing: .3px; }
  .main-nav { position: absolute; right: 131px; top: 52px; display: flex; }
  .main-nav a { display: block; height: 24px; line-height: 24px; padding: 0 14px; font-size: 11px; font-weight: 500; color: var(--ink); text-decoration: none; }
  .main-nav a:last-child { padding-right: 0; }
  .main-nav a.active { background: var(--brand-red); color: var(--white); }

  /* Hero */
  .hero { position: absolute; left: 0; top: 86px; width: 1200px; height: 571px; background: radial-gradient(ellipse at 55% 55%, #b9773a 0%, #6a4426 30%, #2b2320 65%, #17181b 100%); }
  .hero-kicker { position: absolute; left: 0; width: 1200px; top: 201px; text-align: center; font-size: 21px; font-weight: 600; letter-spacing: .5px; }
  .hero-title { position: absolute; left: 0; width: 1200px; top: 228px; text-align: center; font-family: "Orbitron", sans-serif; font-weight: 900; font-size: 40px; letter-spacing: 3px; }
  .hero-btn { position: absolute; left: 500px; top: 298px; width: 195px; height: 45px; background: var(--brand-red); border: 2px solid var(--white); display: flex; align-items: center; justify-content: center; font-family: "Orbitron", sans-serif; font-weight: 900; font-size: 15px; letter-spacing: 1px; }
  .slider-dots { position: absolute; left: 534px; top: 490px; display: flex; gap: 16px; align-items: center; }
  .slider-dots span { width: 10px; height: 10px; border-radius: 50%; background: var(--white); }
  .slider-dots span.current { width: 14px; height: 14px; background: transparent; border: 3px solid var(--white); }

  .rivet-band { position: absolute; left: 0; width: 1200px; height: 26px; background: var(--rivet-band); }

  /* Section titles */
  .section-title { position: absolute; left: 0; width: 1200px; text-align: center; font-family: "Orbitron", sans-serif; font-weight: 900; font-size: 22px; letter-spacing: 2px; }
  .title-rule { position: absolute; left: 579px; width: 42px; height: 3px; background: var(--button-red); }
  .solid-btn { position: absolute; background: var(--button-red); color: var(--white); font-size: 12.5px; font-weight: 700; display: flex; align-items: center; justify-content: center; letter-spacing: .3px; }

  /* Products */
  .products { position: absolute; left: 0; top: 683px; width: 1200px; height: 746px; background: var(--ink); }
  .product-card { position: absolute; width: 298px; height: 226px; }
  .product-card .label { position: absolute; left: 19px; bottom: 15px; font-size: 16px; font-weight: 700; line-height: 1.2; letter-spacing: .4px; }
  .tone-vessel { background: linear-gradient(180deg, #5f6f86 0%, #8a7f8d 50%, #3f3d3c 100%); }
  .tone-tank { background: linear-gradient(180deg, #7f8e87 0%, #a3a9a3 45%, #4a5a3a 100%); }
  .tone-stack { background: linear-gradient(180deg, #c9d0da 0%, #6d86a9 50%, #44597a 100%); }
  .tone-silo { background: linear-gradient(180deg, #9eaab8 0%, #7b828a 50%, #4d5259 100%); }
  .tone-spool { background: linear-gradient(180deg, #7c8a92 0%, #3f5566 50%, #4b4c44 100%); }
  .tone-tower { background: linear-gradient(180deg, #8d9aa6 0%, #b6bec6 45%, #5e6670 100%); }

  /* Services */
  .services { position: absolute; left: 0; top: 1456px; width: 1200px; height: 463px; background: var(--services-bg); }
  .service { position: absolute; top: 175px; width: 200px; margin-left: -100px; text-align: center; }
  .service svg { display: block; margin: 0 auto; width: 60px; height: 60px; }
  .service p { margin-top: 36px; font-size: 15px; line-height: 1.35; }
  .service-divider { position: absolute; top: 157px; width: 1px; height: 159px; background: var(--divider); }

  /* Footer */
  .site-footer { position: absolute; left: 0; top: 1919px; width: 1200px; height: 357px; background: var(--footer-bg); font-family: "Open Sans", sans-serif; }
  .footer-brand { position: absolute; left: 133px; top: 53px; display: flex; align-items: center; gap: 14px; }
  .footer-brand .brand-dot { width: 100px; height: 100px; background: transparent; border: 6px solid var(--white); }
  .footer-brand .brand-name { color: var(--white); font-size: 30px; }
  .footer-heading { position: absolute; top: 62px; font-size: 12px; font-weight: 700; letter-spacing: .3px; }
  .contact-item { position: absolute; left: 482px; display: flex; gap: 11px; font-size: 11px; line-height: 1.6; color: var(--muted); }
  .contact-item svg { width: 11px; height: 12px; margin-top: 3px; flex: none; }
  .footer-menu { position: absolute; left: 720px; top: 94px; list-style: none; font-size: 11px; line-height: 17.6px; color: var(--muted); }
  .start-btn { position: absolute; left: 901px; top: 99px; width: 167px; height: 41px; background: var(--button-red); font-family: "Open Sans", sans-serif; font-size: 15.5px; font-weight: 700; display: flex; align-items: center; justify-content: center; letter-spacing: .5px; }
  .footer-rule { position: absolute; left: 133px; top: 268px; width: 935px; height: 1px; background: #5a5556; }
  .follow { position: absolute; left: 133px; top: 302px; display: flex; align-items: center; gap: 9px; font-size: 12px; font-weight: 700; }
  .follow .label { margin-right: 10px; }
  .social-dot { width: 26px; height: 26px; border-radius: 50%; }
  .social-dot.one { background: #3b5a9a; }
  .social-dot.two { background: #1da1e2; }
  .social-dot.three { background: #1c3f8a; }
  .copyright { position: absolute; right: 132px; top: 308px; font-size: 11px; color: var(--muted); }
</style>
</head>
<body>

<header class="site-header">
  <div class="brand"><span class="brand-dot"></span><span class="brand-name"><span>Marlow</span><span>Ridgeway</span></span></div>
  <div class="call-line">
    <svg width="12" height="12" viewBox="0 0 24 24" aria-hidden="true"><path fill="#6D0B17" d="M6.6 10.8a15.1 15.1 0 0 0 6.6 6.6l2.2-2.2a1 1 0 0 1 1-.25 11.4 11.4 0 0 0 3.6.57 1 1 0 0 1 1 1V20a1 1 0 0 1-1 1A17 17 0 0 1 3 4a1 1 0 0 1 1-1h3.5a1 1 0 0 1 1 1c0 1.25.2 2.45.57 3.57a1 1 0 0 1-.25 1z"/></svg>
    <span>Call us now</span><span class="number">555.014.2390</span>
  </div>
  <div class="quote-btn">REQUEST A QUOTE</div>
  <nav class="main-nav">
    <a class="active">HOME</a><a>ABOUT</a><a>PRODUCTS</a><a>SERVICES</a><a>WHO WE SERVE</a><a>RESOURCES</a><a>CONTACT</a>
  </nav>
</header>

<section class="hero" role="img" aria-label="Laser cutting head throwing bright sparks across a steel plate">
  <div class="hero-kicker">YOUR VISION, OUR CUSTOM QUALITY</div>
  <h1 class="hero-title">FABRICATION SERVICES</h1>
  <div class="hero-btn">VIEW PRODUCT</div>
  <div class="slider-dots"><span></span><span></span><span class="current"></span><span></span><span></span></div>
</section>

<div class="rivet-band" style="top:657px" role="img" aria-label="Riveted steel strip"></div>

<section class="products">
  <h2 class="section-title" style="top:49px">PRODUCTS</h2>
  <div class="title-rule" style="top:89px"></div>

  <div class="product-card tone-vessel" style="left:133px;top:136px" role="img" aria-label="Steel pressure vessel loaded on a truck trailer"><span class="label">ASME STEEL<br>PRESSURE VESSELS</span></div>
  <div class="product-card tone-tank" style="left:452px;top:136px" role="img" aria-label="Stainless steel tank on a trailer"><span class="label">ASME STAINLESS<br>STEEL TANKS</span></div>
  <div class="product-card tone-stack" style="left:771px;top:136px" role="img" aria-label="Exhaust stacks against the sky"><span class="label">EXHAUST STACKS</span></div>
  <div class="product-card tone-silo" style="left:133px;top:382px" role="img" aria-label="Row of steel silos"><span class="label">STEEL SILOS</span></div>
  <div class="product-card tone-spool" style="left:452px;top:382px" role="img" aria-label="Large flanged spool piece"><span class="label">SPOOL PIECES</span></div>
  <div class="product-card tone-tower" style="left:771px;top:382px" role="img" aria-label="Tall steel tower seen from below"><span class="label">TOWERS</span></div>

  <div class="solid-btn" style="left:510px;top:655px;width:179px;height:38px">VIEW ALL PRODUCTS</div>
</section>

<div class="rivet-band" style="top:1429px;height:27px" role="img" aria-label="Riveted steel strip"></div>

<section class="services">
  <h2 class="section-title" style="top:48px">SERVICES</h2>
  <div class="title-rule" style="top:98px"></div>

  <div class="service" style="left:220px">
    <svg viewBox="0 0 60 60" aria-hidden="true"><path fill="#fff" d="M10 46h40l-8-14H26z"/><path fill="#fff" d="M14 14l4-3 16 20-4 3z"/><path fill="#fff" d="M24 12l3-2 3 5-3 2zM18 20l2-3 5 3-2 3z"/><rect x="10" y="48" width="40" height="4" fill="#fff"/></svg>
    <p>Post Weld Heat<br>Treatment</p>
  </div>
  <div class="service-divider" style="left:326px"></div>

  <div class="service" style="left:417px">
    <svg viewBox="0 0 60 60" aria-hidden="true"><rect x="20" y="14" width="28" height="16" rx="3" fill="#fff"/><rect x="30" y="30" width="11" height="22" rx="2" fill="#fff"/><rect x="8" y="20" width="12" height="4" fill="#fff"/><path d="M2 22h6" stroke="#fff" stroke-width="2" stroke-dasharray="2 1"/><rect x="38" y="18" width="4" height="8" fill="#2C2728"/></svg>
    <p>Drilling and<br>Burning</p>
  </div>
  <div class="service-divider" style="left:505px"></div>

  <div class="service" style="left:584px">
    <svg viewBox="0 0 60 60" aria-hidden="true"><rect x="22" y="14" width="22" height="12" rx="3" fill="#fff"/><rect x="28" y="8" width="8" height="6" fill="#fff"/><rect x="30" y="26" width="8" height="18" fill="#fff"/><path d="M38 34c10 0 10 14 0 14h-6" stroke="#fff" stroke-width="3" fill="none"/><circle cx="12" cy="16" r="1.5" fill="#fff"/><circle cx="8" cy="20" r="1.5" fill="#fff"/><circle cx="14" cy="22" r="1.5" fill="#fff"/><circle cx="9" cy="26" r="1.5" fill="#fff"/><circle cx="16" cy="18" r="1.5" fill="#fff"/></svg>
    <p>Coatings</p>
  </div>
  <div class="service-divider" style="left:671px"></div>

  <div class="service" style="left:777px">
    <svg viewBox="0 0 60 60" aria-hidden="true"><g fill="#fff"><circle cx="22" cy="30" r="11"/><g stroke="#fff" stroke-width="6"><path d="M22 14v32M6 30h32M11 19l22 22M33 19L11 41"/></g><circle cx="44" cy="16" r="7"/><g stroke="#fff" stroke-width="4"><path d="M44 6v20M34 16h20M37 9l14 14M51 9L37 23"/></g><circle cx="44" cy="44" r="7"/><g stroke="#fff" stroke-width="4"><path d="M44 34v20M34 44h20M37 37l14 14M51 37L37 51"/></g></g><circle cx="22" cy="30" r="4" fill="#2C2728"/><circle cx="44" cy="16" r="2.5" fill="#2C2728"/><circle cx="44" cy="44" r="2.5" fill="#2C2728"/></svg>
    <p>Non-Destructive<br>Testing</p>
  </div>
  <div class="service-divider" style="left:875px"></div>

  <div class="service" style="left:986px">
    <svg viewBox="0 0 60 60" aria-hidden="true"><path fill="#fff" d="M6 6h48v36H36l-6 8-6-8H6z"/><g fill="#2C2728"><rect x="14" y="15" width="32" height="3"/><rect x="14" y="22" width="32" height="3"/><rect x="14" y="29" width="32" height="3"/></g></svg>
    <p>Learning Additional<br>Information</p>
  </div>

  <div class="solid-btn" style="left:510px;top:375px;width:179px;height:36px">READ MORE SERVICES</div>
</section>

<footer class="site-footer">
  <div class="footer-brand"><span class="brand-dot"></span><span class="brand-name"><span>Marlow</span><span>Ridgeway</span></span></div>

  <div class="footer-heading" style="left:482px">CONTACT US</div>
  <div class="contact-item" style="top:92px">
    <svg viewBox="0 0 24 24" aria-hidden="true"><path fill="#fff" d="M12 2a7 7 0 0 0-7 7c0 5 7 13 7 13s7-8 7-13a7 7 0 0 0-7-7zm0 9.5A2.5 2.5 0 1 1 12 6.5a2.5 2.5 0 0 1 0 5z"/></svg>
    <span>88 Foundry Lane<br>Harlow, IL 60999</span>
  </div>
  <div class="contact-item" style="top:141px">
    <svg viewBox="0 0 24 24" aria-hidden="true"><path fill="#fff" d="M6.6 10.8a15.1 15.1 0 0 0 6.6 6.6l2.2-2.2a1 1 0 0 1 1-.25 11.4 11.4 0 0 0 3.6.57 1 1 0 0 1 1 1V20a1 1 0 0 1-1 1A17 17 0 0 1 3 4a1 1 0 0 1 1-1h3.5a1 1 0 0 1 1 1c0 1.25.2 2.45.57 3.57a1 1 0 0 1-.25 1z"/></svg>
    <span>555.014.2390</span>
  </div>
  <div class="contact-item" style="top:176px">
    <svg viewBox="0 0 24 24" aria-hidden="true"><path fill="#fff" d="M2 5h20v14H2z"/><path d="M2 5l10 8 10-8" stroke="#3D3839" stroke-width="2" fill="none"/></svg>
    <span>info@marlowridgeway.example</span>
  </div>

  <div class="footer-heading" style="left:720px">MENU</div>
  <ul class="footer-menu">
    <li>HOME</li><li>ABOUT</li><li>PRODUCTS</li><li>SERVICES</li><li>WHO WE SERVE</li><li>RESOURCES</li><li>CONTACT</li>
  </ul>

  <div class="footer-heading" style="left:901px">GET IN TOUCH</div>
  <div class="start-btn">START TODAY</div>

  <div class="footer-rule"></div>
  <div class="follow">
    <span class="label">FOLLOW US</span>
    <span class="social-dot one"></span><span class="social-dot two"></span><span class="social-dot three"></span>
  </div>
  <div class="copyright">© 2018 Marlow-Ridgeway. All Rights Reserved.</div>
</footer>

</body>
</html>
```